Organic Infographic – "The 4 Pillars of Renewal"

Overview:
We are a coaching/education brand (Brightmoor Institute) and need a redesigned infographic illustrating our 4-area transformation model. Our current version (attached) uses a rigid, hard-edged triangle/pyramid layout — we want a completely new visual approach that feels organic, soft, and alive, since the topic is human personal development, not a technical process.

Content structure (please keep the wording, redesign the visual form):

4 areas: "Embodiment – The Foundation" and "Focus & Intuition Redefined – The Lens" sit on the same base level. "Heart Centered Living – The Bridge" sits one level above, connecting/enabling the other two. "Becoming Unlimited – The Peak" sits at the top, made possible by Heart Centered Living.
The 4 areas influence and inspire one another — this mutual connection must be visually recognizable (e.g. through overlapping zones, blended color transitions, connecting flowing lines, or similar). Areas may stay visually distinct; the connection between them is what must be shown.
Hierarchy should be expressed mainly through position/arrangement (ascending flow), not through size differences — all 4 areas should carry similar visual weight, since each is equally essential.
A supporting element: "The Brightmoor Methodology" with 3 phases (Phase 1: Awareness & Insight, Phase 2: Integration & Practice, Phase 3: Expansion & Sustainable Growth), each with a short description (text provided below).

Style direction:
Organic, soft, flowing shapes — no sharp angles or rigid geometric triangles. Attached are 3 moodboard references showing the direction we like: overlapping/blended circular shapes, flowing ribbon-style connections, and organic swirl divisions. Please don't copy any of them directly — combine this organic/overlapping visual language with our specific asymmetric hierarchy (2 areas base level + 1 bridge + 1 peak), which none of the references show exactly. This creative translation is the core task.

Icons: Please design one new, unified icon per area (4 total) plus 3 simple icons for the methodology phases — consistent style across all 7, your creative interpretation is welcome.

Typography: Headlines in Arsenal, body text in DM Sans.

Colors: Base palette — Embodiment D09176, Focus & Intuition Redefined B6623E, Heart Centered Living D9866B, Becoming Unlimited 6F7A70, dark text 23211A, light accent EACEC1. Slight adjustments are welcome if they improve visual distinction between areas.

Technical requirements (important):

Final files as vector format (SVG, AI, or EPS), with separated, editable, non-flattened/non-merged layers and paths.
Shapes should consist of simple, closed outline paths — no fine textures, no complex multi-stop gradients, no photorealistic rendering — since the artwork will later be manually redrawn as a whiteboard-animation video.
Primary format: 16:9 landscape. A secondary vertical/mobile version (3 outer areas stacked below the top area) is welcome but optional.

Usage rights: Full commercial usage across website, video, and social media required.

Attachments to include: current draft PDF (for text content and logo reference only — not for layout), our logo file, and the 3 moodboard reference images.

Budget: $100–150 — please let us know if this realistically allows for more designer participation, or advise on adjusting scope/budget

Methodology phase texts (for the 3 supporting icons):

Phase 1: Awareness & Insight
Cultivating self-reflection, identifying patterns, and gaining clarity on personal drivers through introspective practices and data-informed assessment.

Phase 2: Integration & Practice
Applying tools and frameworks, developing new habits, and aligning actions with core values through consistent application and feedback loops.

Phase 3: Expansion & Sustainable Growth
Achieving long-term transformation, exceeding limitations, and fostering resilience through continuous evolution and a purpose-driven approach.

```html
<!DOCTYPE html>
<html lang="en">
<head>
<meta charset="utf-8">
<title>The 4 Pillars of Renewal – Brightmoor Institute</title>
<link href="https://fonts.googleapis.com/css2?family=Arsenal:wght@400;700&family=DM+Sans:wght@400;500&display=swap" rel="stylesheet">
<style>
  :root{
    --stage:#9b9b9b;
    --paper:#f8ece6;
    --paper-warm:#fbf1ea;
    --terracotta:#b95f3d;
    --embodiment:#d09176;
    --embodiment-light:#e4ae9b;
    --heart:#d9866b;
    --focus:#b6623e;
    --unlimited:#6f7a70;
    --sage:#6f7a70;
    --ink:#23211a;
    --accent:#eacec1;
    --white:#ffffff;
  }
  *{margin:0;padding:0;box-sizing:border-box;}
  html,body{width:1200px;height:1200px;overflow:hidden;background:var(--stage);}
  .slide{
    position:absolute;left:0;top:262px;width:1200px;height:675px;overflow:hidden;
    background:radial-gradient(ellipse at 55% 30%, var(--paper-warm) 0%, var(--paper) 60%, #f3e6e0 100%);
    font-family:"DM Sans",sans-serif;color:var(--ink);
  }
  .pillars-title{
    position:absolute;left:76px;top:56px;
    font-family:"Arsenal",sans-serif;font-weight:700;font-size:54px;line-height:52px;
  }
  .pillars-title .line-1{color:var(--terracotta);display:block;}
  .pillars-title .line-2{color:var(--sage);display:block;}
  .title-rule{position:absolute;left:76px;top:187px;width:66px;height:4px;background:var(--terracotta);}
  .pillars-diagram{position:absolute;left:0;top:0;width:620px;height:675px;}
  .arc-label{font-family:"Arsenal",sans-serif;font-weight:700;font-size:15px;fill:var(--ink);}
  .sub-label{font-family:"DM Sans",sans-serif;font-size:12px;fill:var(--ink);}
  .icon-line{fill:none;stroke:var(--ink);stroke-width:1.7;stroke-linecap:round;stroke-linejoin:round;}

  .method-title{
    position:absolute;left:669px;top:66px;
    font-family:"Arsenal",sans-serif;font-size:36px;color:var(--sage);white-space:nowrap;
  }
  .method-title strong{color:var(--terracotta);font-weight:700;}
  .phase{position:absolute;left:665px;width:520px;height:120px;}
  .phase-badge{position:absolute;left:0;top:0;width:64px;height:64px;}
  .phase-pill{
    position:absolute;left:40px;top:0;width:106px;height:23px;border-radius:0 12px 0 0;
    background:var(--sage);color:var(--white);
    font-family:"Arsenal",sans-serif;font-weight:700;font-size:15px;line-height:23px;padding-left:38px;
  }
  .phase-heading{
    position:absolute;left:75px;top:20px;white-space:nowrap;
    font-family:"Arsenal",sans-serif;font-weight:700;font-size:27px;color:var(--terracotta);
  }
  .phase-text{position:absolute;left:76px;top:60px;width:420px;font-size:12.6px;line-height:17.6px;}
  .brand{position:absolute;left:666px;top:543px;display:flex;align-items:center;gap:12px;}
  .brand-dot{width:62px;height:62px;border-radius:50%;background:var(--embodiment);}
  .brand-name{font-family:"Arsenal",sans-serif;font-size:32px;color:var(--sage);}
</style>
</head>
<body>
<main class="slide">
  <h1 class="pillars-title"><span class="line-1">The 4 Pillars of</span><span class="line-2">Renewal</span></h1>
  <div class="title-rule"></div>

  <svg class="pillars-diagram" viewBox="0 0 620 675" aria-label="Four connected pillars rising from foundation to peak">
    <defs>
      <linearGradient id="ribbonGradient" gradientUnits="userSpaceOnUse" x1="80" y1="0" x2="600" y2="0">
        <stop offset="0" stop-color="#e6b4a3"/>
        <stop offset="0.28" stop-color="#d9866b"/>
        <stop offset="0.62" stop-color="#b25d3a"/>
        <stop offset="1" stop-color="#6f7a70"/>
      </linearGradient>
      <filter id="discShadow" x="-30%" y="-30%" width="160%" height="160%">
        <feDropShadow dx="3" dy="4" stdDeviation="3" flood-color="#000" flood-opacity="0.28"/>
      </filter>
    </defs>

    <g class="ribbon">
      <path d="M157,479 C220,479 216,318 279,318 C342,318 337,479 400,479 C463,479 459,318 522,318"
            fill="none" stroke="url(#ribbonGradient)" stroke-width="74" stroke-linecap="round"/>
      <circle cx="157" cy="479" r="75" fill="url(#ribbonGradient)"/>
      <circle cx="279" cy="318" r="75" fill="url(#ribbonGradient)"/>
      <circle cx="400" cy="479" r="75" fill="url(#ribbonGradient)"/>
      <circle cx="522" cy="318" r="75" fill="url(#ribbonGradient)"/>
    </g>

    <g class="discs" filter="url(#discShadow)" fill="var(--white)">
      <circle cx="157" cy="479" r="55"/>
      <circle cx="279" cy="318" r="55"/>
      <circle cx="400" cy="479" r="55"/>
      <circle cx="522" cy="318" r="55"/>
    </g>

    <!-- Embodiment icon: grounded drop -->
    <g class="icon-line" transform="translate(157 479)">
      <path d="M0,-26 C10,-12 18,-2 18,8 A18,18 0 0 1 -18,8 C-18,-2 -10,-12 0,-26 Z"/>
      <path d="M-8,8 A8,8 0 0 0 8,8"/>
      <path d="M-24,30 H24"/>
    </g>
    <!-- Heart Centered Living icon: heart with pulse -->
    <g class="icon-line" transform="translate(279 318)">
      <path d="M0,20 C-22,6 -28,-6 -24,-15 C-20,-24 -7,-25 0,-14 C7,-25 20,-24 24,-15 C28,-6 22,6 0,20 Z"/>
      <path d="M-20,-2 H-8 L-4,-10 L2,6 L6,-2 H20"/>
    </g>
    <!-- Focus & Intuition icon: target -->
    <g class="icon-line" transform="translate(400 479)">
      <circle r="22"/>
      <circle r="12"/>
      <circle r="3"/>
      <path d="M0,-30 V-18 M0,18 V30 M-30,0 H-18 M18,0 H30"/>
    </g>
    <!-- Becoming Unlimited icon: infinity over open palm line -->
    <g class="icon-line" transform="translate(522 318)">
      <path d="M0,-8 C-6,-18 -20,-18 -20,-8 C-20,2 -6,2 0,-8 C6,-18 20,-18 20,-8 C20,2 6,2 0,-8 Z"/>
      <path d="M-26,16 C-12,24 12,24 26,16"/>
    </g>

    <path id="arcHeart" d="M196,228 Q279,172 362,228" fill="none"/>
    <path id="arcUnlimited" d="M439,228 Q522,172 605,228" fill="none"/>
    <path id="arcFocus" d="M318,538 Q400,602 482,538" fill="none"/>

    <text class="arc-label"><textPath href="#arcHeart" startOffset="50%" text-anchor="middle">Heart Centered Living</textPath></text>
    <text class="sub-label" x="279" y="230" text-anchor="middle">The Bridge</text>

    <text class="arc-label"><textPath href="#arcUnlimited" startOffset="50%" text-anchor="middle">Becoming Unlimited</textPath></text>
    <text class="sub-label" x="522" y="230" text-anchor="middle">The Peak</text>

    <text class="arc-label" x="153" y="574" text-anchor="middle">Embodiment</text>
    <text class="sub-label" x="153" y="596" text-anchor="middle">The Foundation</text>

    <text class="arc-label"><textPath href="#arcFocus" startOffset="50%" text-anchor="middle">Focus &amp; Intuition Redefined</textPath></text>
    <text class="sub-label" x="400" y="596" text-anchor="middle">The Foundation</text>
  </svg>

  <h2 class="method-title">The Brightmoor <strong>Methodology</strong></h2>

  <section class="phase" style="top:132px;">
    <div class="phase-pill">Phase 1</div>
    <svg class="phase-badge" viewBox="0 0 64 64" aria-hidden="true">
      <circle cx="32" cy="32" r="31" fill="var(--embodiment)"/>
      <circle cx="32" cy="32" r="26" fill="none" stroke="var(--accent)" stroke-width="1.5"/>
      <g fill="none" stroke="var(--white)" stroke-width="1.6" stroke-linecap="round">
        <path d="M26,30 A8,8 0 1 1 38,30 C36,33 36,35 36,37 H28 C28,35 28,33 26,30 Z"/>
        <path d="M28,41 H36 M29,44 H35"/>
      </g>
    </svg>
    <div class="phase-heading">Awareness &amp; Insight</div>
    <p class="phase-text">Cultivating self-reflection, identifying patterns and gaining clarity on personal drivers through introspective practices and data-informed assessment.</p>
  </section>

  <section class="phase" style="top:264px;">
    <div class="phase-pill">Phase 2</div>
    <svg class="phase-badge" viewBox="0 0 64 64" aria-hidden="true">
      <circle cx="32" cy="32" r="31" fill="var(--embodiment)"/>
      <circle cx="32" cy="32" r="26" fill="none" stroke="var(--accent)" stroke-width="1.5"/>
      <g fill="none" stroke="var(--white)" stroke-width="1.6" stroke-linecap="round">
        <circle cx="26" cy="27" r="5"/>
        <path d="M26,19 V21 M26,33 V35 M18,27 H20 M32,27 H34"/>
        <circle cx="39" cy="39" r="5"/>
        <path d="M39,31 V33 M39,45 V47 M31,39 H33 M45,39 H47"/>
      </g>
    </svg>
    <div class="phase-heading">Integration &amp; Practice</div>
    <p class="phase-text">Applying tools and frameworks, developing new habits and aligning actions with core values through consistent application and feedback loops.</p>
  </section>

  <section class="phase" style="top:400px;">
    <div class="phase-pill">Phase 3</div>
    <svg class="phase-badge" viewBox="0 0 64 64" aria-hidden="true">
      <circle cx="32" cy="32" r="31" fill="var(--embodiment)"/>
      <circle cx="32" cy="32" r="26" fill="none" stroke="var(--accent)" stroke-width="1.5"/>
      <g fill="none" stroke="var(--white)" stroke-width="1.6" stroke-linecap="round">
        <circle cx="32" cy="32" r="12"/>
        <ellipse cx="32" cy="32" rx="5" ry="12"/>
        <path d="M20,32 H44"/>
        <path d="M17,17 L21,21 M47,17 L43,21 M17,47 L21,43 M47,47 L43,43"/>
      </g>
    </svg>
    <div class="phase-heading">Expansion &amp; Sustainable Growth</div>
    <p class="phase-text">Achieving long-term transformation, exceeding limitations and fostering resilience through continuous evolution and a purpose-driven approach.</p>
  </section>

  <div class="brand">
    <span class="brand-dot"></span>
    <span class="brand-name">Brightmoor Institute</span>
  </div>
</main>
</body>
</html>
```